Artificial intelligence, machine learning, and automation company needs a sexy business card design

We need a sleek and sexy business card design for an AI consulting company based in Philadelphia PA. We provide custom machine learning and automation solutions for companies of all shapes and sizes. The primary industries that we serve are pharmaceuticals, engineering, healthcare, and computer software. We would like the designs to be a black business card that uses green as a sleek accent color. The final design should communicate intelligence, cutting edge new-tech, and optimization.

Target Market(s)

C-level and VP level executives of multi-million annual companies. Mostly in Pharma, Healthcare, Real Estate, Retail, and Engineering

Industry/Entity Type

Computer Software

Contact Information for Business Card

Name: Jack Moss
Title: CEO
Cell: 215 604 8293
Email: JackM@quillarcworks.example
Website: www.QuillarcWorks.example

Font styles to use
Sans Serif

Colors

Designer to choose colors to be used in the design.

Requirements
Must have
• 1) Attached Quillarc Logo (either with colors or not/embossed)
• 2) "Artificial Intelligence" "Automation" and "Machine Learning"
• 3) "Quillarc Laboratories" or "Quillarc Works" or "Quillarc"
• 4) Sexy AF.
Nice to have
• Black card / dark card color, "Quillarc Green" accent colors (in attached .ai file), Embossment of logo/name/etc, thick card stock, colored borders (on card sides, not front/back faces)
Should not have
• Should not be bland, or unsexy.

```html
<!DOCTYPE html>
<html lang="en">
<head>
<meta charset="utf-8">
<title>Quillarc Laboratories — Business Card</title>
<link rel="stylesheet" href="https://fonts.googleapis.com/css2?family=Questrial&family=Didact+Gothic&display=swap">
<style>
  :root {
    --bg: #2a2522;
    --card-front: #141416;
    --card-back: #2b2b2d;
    --accent: #4fc7b3;
    --text-light: #e8e8e8;
    --text-dim: #8a8a8c;
    --logo-tone: #9a9a9e;
  }
  * { margin: 0; padding: 0; box-sizing: border-box; }
  html, body { width: 1200px; height: 715px; overflow: hidden; background: var(--bg); }
  .canvas {
    width: 1200px; height: 715px;
    display: flex; align-items: center; justify-content: center; gap: 60px;
  }
  .card {
    position: relative;
    width: 500px; height: 286px;
    border-radius: 3px;
    box-shadow: 0 18px 40px rgba(0,0,0,.55);
    overflow: hidden;
  }
  /* Front face */
  .card--front { background: var(--card-front); }
  .brand {
    position: absolute; left: 92px; top: 88px;
    display: flex; align-items: center; gap: 18px;
  }
  .brand__mark {
    width: 58px; height: 58px;
    border: 3px solid var(--logo-tone);
  }
  .brand__name {
    font-family: "Questrial", sans-serif;
    color: var(--logo-tone);
    line-height: 1;
  }
  .brand__name-main { display: block; font-size: 40px; letter-spacing: 8px; }
  .brand__name-sub { display: block; font-size: 17px; letter-spacing: 6px; margin-top: 6px; }
  .tagline {
    position: absolute; left: 0; right: 0; top: 196px;
    text-align: center;
    font-family: "Didact Gothic", sans-serif;
    font-size: 13px; color: var(--text-dim); letter-spacing: .3px;
  }
  /* Back face */
  .card--back { background: var(--card-back); }
  .card__band {
    position: absolute; left: 0; right: 0; bottom: 0; height: 11px;
    background: var(--accent);
  }
  .holder {
    position: absolute; right: 315px; top: 110px; text-align: right;
    font-family: "Questrial", sans-serif;
  }
  .holder__name { font-size: 22px; color: var(--accent); font-weight: 700; white-space: nowrap; }
  .holder__title { font-size: 13px; color: var(--text-light); margin-top: 6px; }
  .divider {
    position: absolute; left: 204px; top: 104px; width: 2px; height: 62px;
    background: linear-gradient(to bottom, transparent, var(--accent), transparent);
  }
  .contact {
    position: absolute; left: 228px; top: 100px; right: 16px;
    font-family: "Didact Gothic", sans-serif; font-size: 13px; color: var(--text-light);
    list-style: none; white-space: nowrap;
  }
  .contact__item { display: flex; align-items: center; gap: 9px; height: 24px; }
  .contact__icon { width: 17px; height: 17px; flex: none; }
  .contact__web {
    font-family: "Questrial", sans-serif; font-weight: 700;
    font-size: 14px; color: var(--accent); margin-top: 6px; letter-spacing: .3px;
  }
</style>
</head>
<body>
<main class="canvas">
  <section class="card card--front" aria-label="Card front">
    <div class="brand">
      <div class="brand__mark"></div>
      <p class="brand__name">
        <span class="brand__name-main">QUILLARC</span>
        <span class="brand__name-sub">LABORATORIES</span>
      </p>
    </div>
    <p class="tagline">Artificial Intelligence, Automation and Machine Learning</p>
  </section>

  <section class="card card--back" aria-label="Card back">
    <div class="holder">
      <p class="holder__name">Jack Moss</p>
      <p class="holder__title">CEO</p>
    </div>
    <div class="divider"></div>
    <ul class="contact">
      <li class="contact__item">
        <svg class="contact__icon" viewBox="0 0 20 20" aria-hidden="true">
          <circle cx="10" cy="10" r="10" fill="var(--accent)"/>
          <path d="M5 8.5c0-1.2 2.2-2.3 5-2.3s5 1.1 5 2.3l-1.6.6-.6-1.4H7.2l-.6 1.4z M6.5 10h7l.8 4h-8.6z" fill="#2b2b2d"/>
        </svg>
        <span>215 604 8293</span>
      </li>
      <li class="contact__item">
        <svg class="contact__icon" viewBox="0 0 20 20" aria-hidden="true">
          <circle cx="10" cy="10" r="10" fill="var(--accent)"/>
          <rect x="5" y="6.5" width="10" height="7" fill="none" stroke="#2b2b2d" stroke-width="1.4"/>
          <path d="M5 6.5l5 4 5-4" fill="none" stroke="#2b2b2d" stroke-width="1.4"/>
        </svg>
        <span>JackM@quillarcworks.example</span>
      </li>
      <li class="contact__web">www.QuillarcWorks.example</li>
    </ul>
    <div class="card__band"></div>
  </section>
</main>
</body>
</html>
```